TWH Business Card Design Project

Real Estate Broker, Realtor
I would like something similar to what I have attached from Fenwick Realty except my company is Corvale Realty Group, LLC. Instead of a single "B" on the back I would like "TWH". Phone # 555-214-7093
Name - Dalton Marsh
Licensed in the State of Missouri
No address
email - dmarsh@corvalerealtyexample.com
Contact Information for Business Card
I would like something similar to what I have attached from Fenwick Realty except my company is Corvale Realty Group, LLC. Instead of a single "B" on the back I would like "TWH". Phone # 816-863-7093Name - Dalton YiLicensed in the State of MissouriNo addressemail - dmarsh@corvalerealtyexample.com

```html
<!DOCTYPE html>
<html lang="en">
<head>
<meta charset="utf-8">
<title>Corvale Realty Group – Business Card</title>
<link rel="stylesheet" href="https://fonts.googleapis.com/css2?family=Montserrat:wght@300;400;600;700&display=swap">
<style>
  :root {
    --backdrop: #d1d2d4;
    --card-brown: #3e3830;
    --brand-blue: #48aed8;
    --ink-white: #ffffff;
    --rule-grey: #b9b6b0;
  }
  * { margin: 0; padding: 0; box-sizing: border-box; }
  html, body { width: 1200px; height: 1000px; overflow: hidden; }
  body {
    position: relative;
    background: var(--backdrop);
    font-family: "Montserrat", Arial, sans-serif;
  }
  .card {
    position: absolute;
    top: 201px;
    width: 342px;
    height: 598px;
    overflow: hidden;
    text-align: center;
  }
  .card-front { left: 229px; background: var(--card-brown); color: var(--ink-white); }
  .card-back { left: 630px; background: var(--brand-blue); }

  .line { position: absolute; left: 0; width: 100%; white-space: nowrap; }

  .brand-dot {
    position: absolute; left: 140px; top: 23px;
    width: 62px; height: 62px; border-radius: 50%;
    background: var(--brand-blue);
  }
  .company-name {
    top: 92px; font-size: 26px; font-weight: 600;
    line-height: 38px; letter-spacing: 1px; text-transform: uppercase;
  }
  .phone { top: 221px; font-size: 35px; font-weight: 700; color: var(--brand-blue); }
  .agent-name { top: 284px; font-size: 31px; font-weight: 400; }
  .agent-title { top: 323px; font-size: 15px; font-weight: 400; color: var(--brand-blue); }
  .mail-icon { position: absolute; left: 154px; top: 363px; width: 34px; height: 24px; }
  .email { top: 394px; font-size: 16.5px; font-weight: 400; }
  .licence { top: 445px; font-size: 15px; font-weight: 400; color: var(--brand-blue); }
  .divider { position: absolute; left: 0; top: 508px; width: 100%; height: 2px; background: var(--rule-grey); }
  .website-front { top: 542px; font-size: 17px; font-weight: 700; color: var(--brand-blue); }

  .back-disc {
    position: absolute; left: -30px; top: 31px;
    width: 402px; height: 402px; border-radius: 50%;
    background: var(--card-brown);
  }
  .initials {
    top: 160px; font-size: 128px; line-height: 1;
    font-weight: 600; color: var(--brand-blue); letter-spacing: -2px;
  }
  .website-back { top: 536px; font-size: 17px; font-weight: 700; color: var(--card-brown); }
</style>
</head>
<body>
  <section class="card card-front">
    <div class="brand-dot"></div>
    <div class="line company-name">Corvale<br>Realty Group, LLC</div>
    <div class="line phone">555-214-7093</div>
    <div class="line agent-name">Dalton Marsh</div>
    <div class="line agent-title">Principal Broker</div>
    <svg class="mail-icon" viewBox="0 0 34 24" aria-hidden="true">
      <rect x="1" y="1" width="32" height="22" fill="none" stroke="#ffffff" stroke-width="1.6"/>
      <polyline points="1,1 17,14 33,1" fill="none" stroke="#ffffff" stroke-width="1.6"/>
    </svg>
    <div class="line email">dmarsh@corvalerealtyexample.com</div>
    <div class="line licence">Licensed in the State of Missouri</div>
    <div class="divider"></div>
    <div class="line website-front">CorvaleRealtyExample.com</div>
  </section>

  <section class="card card-back">
    <div class="back-disc"></div>
    <div class="line initials">TWH</div>
    <div class="line website-back">CorvaleRealtyExample.com</div>
  </section>
</body>
</html>
```